ZEPHIRO needs a new business card!

ZEPHIRO is a group of gaming enthusiasts who are looking for a new corporate business card.

The typeface should be modern and minimalist with attention paid to spacing between the letters and the letters 'zephiro' look relative to each other.

Should clean, crisp and minimalist - looking serious overall but with slight tweaks to the letters to make them look playful...

Black on white is fine.

Details on the card should include:
-the word 'zephiro'
-a job title (use any, for e.g. founder)
-a name (e.g. Ned Falka)
-phone number
-email address

For inspiration: http://brisket.tumblevane-cdn.example/wp-content/uploads/2013/07/mela-1.jpg

Target Market(s)

Video gaming enthusiasts

Industry/Entity Type

Business

Requirements
Must have
• Black letter on white background.
The word "zephiro"
Nice to have
• Maybe use a conservative font like Gibraltar or Helvetica and tweaking each letter individually.

You can insert normal job titles under the "zephiro" typeface
Should not have
• Should not be cartoony or childish fonts. No colors.

```html
<!DOCTYPE html>
<html lang="en">
<head>
<meta charset="utf-8">
<title>ZEPHIRO — Business Card</title>
<link rel="stylesheet" href="https://fonts.googleapis.com/css2?family=Roboto+Condensed:wght@400;500&display=swap">
<style>
  :root {
    --ink: #0d0d0d;
    --paper: #ffffff;
  }
  html, body {
    margin: 0;
    padding: 0;
    width: 1200px;
    height: 693px;
    overflow: hidden;
    background: var(--paper);
  }
  .business-card {
    position: relative;
    width: 1200px;
    height: 693px;
    background: var(--paper);
    color: var(--ink);
    font-family: "Roboto Condensed", "Arial Narrow", sans-serif;
  }
  .wordmark {
    position: absolute;
    left: 0;
    right: 0;
    top: 38px;
    margin: 0;
    text-align: center;
    font-weight: 500;
    font-size: 218px;
    line-height: 1;
    letter-spacing: 0.11em;
    padding-left: 0.11em;
    color: var(--ink);
  }
  .contact {
    position: absolute;
    left: 0;
    right: 0;
    top: 328px;
    margin: 0;
    text-align: center;
    font-style: normal;
    font-weight: 400;
    font-size: 58px;
    line-height: 59px;
    color: var(--ink);
  }
  .contact span {
    display: block;
  }
  .contact .phone {
    letter-spacing: 0.03em;
  }
</style>
</head>
<body>
  <main class="business-card">
    <h1 class="wordmark">ZEPHIRO</h1>
    <address class="contact">
      <span class="name">Ned Falka</span>
      <span class="job-title">Founder</span>
      <span class="phone">(234)-555-0147</span>
      <span class="email">nedfalka@zephiro.com</span>
    </address>
  </main>
</body>
</html>
```